New Business Card Design Project

Looking for a modern business card design for an import distribution business for industrial technical products. The winning design will translate modern, sophistication, technical, professional and sustainable.

Target Market(s)

Technical customers

Industry/Entity Type

Business

Contact Information for Business Card

Dean Harlow
Sales Manager
M: 0471 625 183
P: 1300 872 619
dean@volkarsystems.com.au
4/18 Galloway Crest Road
Larchfield NSW 2158
www.volkarsystems.com.au

Font styles to use
Sans Serif

Colors
ec1f27
606060
000000
fbfbfb

Requirements
Must have
• My Logo which is the Volkar Systems logo attached
Nice to have
• Eurostile Bold font

```html
<!DOCTYPE html>
<html lang="en">
<head>
<meta charset="utf-8">
<title>Volkar Systems – Business Card</title>
<link href="https://fonts.googleapis.com/css2?family=Lato:wght@400;700;900&display=swap" rel="stylesheet">
<style>
  :root {
    --brand-red: #ec1f27;
    --text-grey: #606060;
    --ink: #000000;
    --paper: #ffffff;
    --backdrop: #eeeeee;
    --tint: #fbe1dc;
  }
  * { box-sizing: border-box; margin: 0; padding: 0; }
  html, body {
    width: 1200px; height: 900px; overflow: hidden;
    background: var(--backdrop);
    font-family: "Lato", sans-serif;
  }
  .stage {
    width: 1200px; height: 900px;
    display: flex; align-items: center; justify-content: center; gap: 60px;
  }
  .card {
    position: relative;
    width: 520px; height: 318px;
    border-radius: 3px;
    box-shadow: 0 6px 18px rgba(0,0,0,0.12);
    overflow: hidden;
  }
  .card--front { background: var(--paper); }
  .card--back { background: var(--brand-red); }

  .brand {
    position: absolute; top: 40px; left: 150px;
    display: flex; align-items: center; gap: 10px;
  }
  .brand__square { width: 30px; height: 30px; background: var(--brand-red); }
  .brand__name {
    font-weight: 900; font-size: 28px; letter-spacing: 1px;
    color: var(--brand-red); text-transform: uppercase; white-space: nowrap;
  }
  .tint-block {
    position: absolute; right: 24px; top: 110px;
    width: 130px; height: 130px; background: var(--tint);
  }
  .contact {
    position: absolute; left: 34px; bottom: 30px;
    color: var(--text-grey); font-size: 13px; line-height: 1.45;
  }
  .contact__name { color: var(--brand-red); font-weight: 700; font-size: 19px; line-height: 1.2; }
  .contact__role { margin-bottom: 10px; }
  .contact__address { margin-bottom: 8px; }
  .contact__line { display: flex; align-items: center; gap: 8px; }
  .contact__line svg { width: 11px; height: 11px; flex: none; }
  .accent { color: var(--brand-red); }

  .back-mark {
    position: absolute; top: 50%; left: 50%;
    width: 22px; height: 22px; margin: -11px 0 0 -11px;
    background: var(--paper);
  }
</style>
</head>
<body>
<main class="stage">
  <section class="card card--front" aria-label="Business card front">
    <div class="brand">
      <span class="brand__square"></span>
      <span class="brand__name">Volkar Systems</span>
    </div>
    <div class="tint-block" aria-hidden="true"></div>
    <div class="contact">
      <p class="contact__name">Dean Harlow</p>
      <p class="contact__role">Sales Manager</p>
      <p class="contact__address">4/18 Galloway Crest Road<br>Larchfield NSW 2158</p>
      <p class="contact__line">
        <svg viewBox="0 0 12 12"><rect x="3" y="1" width="6" height="10" rx="1" fill="none" stroke="#ec1f27" stroke-width="1.4"/></svg>
        0471 625 183
      </p>
      <p class="contact__line">
        <svg viewBox="0 0 12 12"><path d="M2 1.5 L4.5 1.5 L5.5 4 L4 5 Q5 7.5 7 8 L8 6.5 L10.5 7.5 L10.5 10 Q5 11 2 5 Z" fill="#ec1f27"/></svg>
        1300 872 619
      </p>
      <p class="contact__line">
        <svg viewBox="0 0 12 12"><circle cx="6" cy="6" r="5.5" fill="#ec1f27"/><path d="M3 4.5 L6 7 L9 4.5" stroke="#fff" stroke-width="1" fill="none"/></svg>
        dean@volkarsystems.com.au
      </p>
      <p class="contact__line">
        <svg viewBox="0 0 12 12"><circle cx="6" cy="6" r="5" fill="none" stroke="#ec1f27" stroke-width="1.3"/><path d="M1 6 H11 M6 1 Q3 6 6 11 M6 1 Q9 6 6 11" stroke="#ec1f27" stroke-width="0.9" fill="none"/></svg>
        <span>www.<span class="accent">volkarsystems</span>.com.au</span>
      </p>
    </div>
  </section>

  <section class="card card--back" aria-label="Business card back">
    <span class="back-mark" aria-hidden="true"></span>
  </section>
</main>
</body>
</html>
```